Renewable energy company needs modern memorable marketing brochure

We have an 8 page marketing brochure which was created in house. This needs to be revamped and modernised to stand out from our competitors in Australia, Chile and the UK. The brochure should depict us as a professional and dynamic company and instil confidence in prospective clients that we do a professional job. Once the design is finalised we will need a country specific document in the correct language i.e. Spanish for Chile. We are happy to pay for these iterations. We have a company logo which we would like incorporated into the brochure and the colours from the logo utilised where appropriate in the overall design. I have uploaded our existing brochure for an example of the content that the brochure needs to have and can upload the images separately if they are needed. Images in the brochure need to be copyright free and we have lots of photos in-house. I have added all the images from the last brochure and also the text in Indesign so it can be copied easily if needed.

Target Market(s)

landowners and companies

Industry/Entity Type

It Company

Requirements
Must have
• A clean modern look with some colours taken from the logo colour. Be easy to print in various countries.

```html
<!DOCTYPE html>
<html lang="en">
<head>
<meta charset="utf-8">
<title>Infinite Energy – Brochure Cover</title>
<link href="https://fonts.googleapis.com/css2?family=Lato:wght@400;700&display=swap" rel="stylesheet">
<style>
  :root {
    --page-bg: #e9e7e3;
    --paper: #ffffff;
    --teal: #1f9c84;
    --teal-light: #35a895;
    --teal-deep: #168a74;
    --ink-light: #ffffff;
    --ink-dark: #333d3b;
    --photo-blue: #5b93d3;
    --photo-sky: #9cc9ec;
    --photo-green: #86c24a;
  }
  * { margin: 0; padding: 0; box-sizing: border-box; }
  html, body {
    width: 1200px;
    height: 803px;
    overflow: hidden;
    background: var(--page-bg);
    font-family: "Lato", Arial, sans-serif;
  }
  .canvas {
    position: relative;
    width: 1200px;
    height: 803px;
    display: flex;
    align-items: center;
    justify-content: center;
  }
  .brochure-cover {
    position: relative;
    width: 510px;
    height: 722px;
    background: var(--paper);
    box-shadow: 0 10px 30px rgba(0, 0, 0, 0.18);
    overflow: hidden;
  }
  .cover-photo {
    position: absolute;
    left: 0; top: 0;
    width: 100%;
    height: 336px;
    background: linear-gradient(135deg, var(--photo-blue) 0%, var(--photo-sky) 45%, var(--photo-green) 100%);
  }
  .cover-band {
    position: absolute;
    left: 0; top: 342px;
    width: 100%;
    height: 248px;
    background: linear-gradient(90deg, var(--teal-deep) 0%, var(--teal) 45%, var(--teal-light) 100%);
    padding: 96px 0 0 60px;
    color: var(--ink-light);
  }
  .cover-title {
    font-weight: 700;
    font-size: 33px;
    letter-spacing: 0.5px;
    line-height: 1;
    text-transform: uppercase;
  }
  .cover-subtitle {
    margin-top: 14px;
    font-weight: 700;
    font-size: 15px;
    line-height: 1.35;
    text-transform: uppercase;
    max-width: 300px;
  }
  .cover-footer {
    position: absolute;
    left: 0; top: 590px;
    width: 100%;
    height: 132px;
    background: var(--paper);
  }
  .cover-web {
    position: absolute;
    right: 26px;
    top: 14px;
    font-size: 10.5px;
    color: var(--ink-dark);
    letter-spacing: 0.2px;
  }
  .brand {
    position: absolute;
    left: 26px;
    bottom: 30px;
    display: flex;
    align-items: center;
    gap: 12px;
  }
  .brand-dot {
    width: 40px;
    height: 40px;
    border-radius: 50%;
    background: var(--teal);
  }
  .brand-name {
    font-weight: 400;
    font-size: 14px;
    line-height: 1.05;
    letter-spacing: 0.5px;
    color: var(--ink-dark);
    text-transform: uppercase;
  }
</style>
</head>
<body>
  <main class="canvas">
    <article class="brochure-cover">
      <div class="cover-photo" role="img" aria-label="Cover photograph: solar panels beside a green grass field under a sunny blue sky"></div>
      <section class="cover-band">
        <h1 class="cover-title">Infinite Energy</h1>
        <p class="cover-subtitle">Use your land to harvest energy from the sun</p>
      </section>
      <footer class="cover-footer">
        <p class="cover-web">www.radiantfields.com.au</p>
        <div class="brand">
          <span class="brand-dot"></span>
          <span class="brand-name">Radiant<br>Fields</span>
        </div>
      </footer>
    </article>
  </main>
</body>
</html>
```